Modern & Simple Essential Oils Label

Company Name: Verdant Hollow

What we sell: Aromatherapy products, pure therapeutic essential oils.

Design need:
We are looking for a creative and youthful design for the labels used on small essentials oils.

I have two sizes of bottles that I use for essential oils a 5ml bottle and a 15ml bottle. They are dark Amber color glass with black lids. I like the clear labels or mayble a dark brown background. With white or clear lettering with punch of color too! Each oil type is represented by different color. (lavender- purple, lemon - yellow). The label will be the same for all the oils in the two sizes with only a different oil name & coordinating color.
5ml label size should be: 1 " x 2.625"
15ml label size should be: 1.5" x 3.5"

I have some labels that I have had another designer start on, but they aren't quite what I want and missing that something (alot!).. I don't know what. Interest maybe? Lack of design? I dunno.. they are attached. Maybe it's the logo? I don't know! But its gotta change! When I cut out a proof and put a sample on the bottle as I look straight on at the label all I see is a big dot, no logo.. nothing interesting.
Updates

Project Deadline Extended
Reason: Hi! Id like to extend this deadline. Ive been unavailable for a few days due to an illness and Im so far behind! Im feeling MUCH better and looking forward to getting caught up and move with the project. Im not sure how this works, but I attached a list of the oils that we currently have available. And in the list is the idea for the color schemes for the oils. The basic idea is for it to have a wide array of colors, so using different shades of greens, yellows, oranges and so on. So that its like a rainbow. We are not set of that particular color for that particular oil. It was just a idea list of possible colors for oils. Thanks so much!

Target Market(s)

Metro & Modern people. Interested in healthy organic living, Mostly women (some men) 20-45 who are interested in holistic healing.

Industry/Entity Type

It Company

Requirements
Must have
• A reputable look. Clean, organic, crisp, zen or spa-like feel. Modern, youthful appealing label design. Approachable and interesting, not intimidating so that I don't turn away people who are new or not familiar with how to use essential oils.
Should not have
• do NOT want the look to be anywhere close to medicinal, witchy, crafty, hippie, mystical, overly earthy, magical, or voodoo. Do not want it to look like something out of a grandmothers medicine cabinet.

```html
<!DOCTYPE html>
<html lang="en">
<head>
<meta charset="utf-8">
<title>Verdant Hollow – Essential Oil Labels</title>
<link rel="stylesheet" href="https://fonts.googleapis.com/css2?family=Questrial&family=Josefin+Slab:wght@400;600&family=Nunito+Sans:wght@300;700&display=swap">
<style>
  :root {
    --bg-centre: #ffffff;
    --bg-edge: #d9d9d9;
    --label-brown: #4f2914;
    --lemon: #cfd51f;
    --lavender: #ab8bc3;
    --band-ink: #4f2914;
    --band-ink-soft: #8a6a3c;
    --band-ink-soft-lav: #e9dff2;
  }
  * { margin: 0; padding: 0; box-sizing: border-box; }
  html, body { width: 1200px; height: 900px; overflow: hidden; }
  body {
    background: radial-gradient(ellipse at center, var(--bg-centre) 40%, var(--bg-edge) 100%);
    position: relative;
    font-family: "Questrial", sans-serif;
  }

  .label {
    position: absolute;
    background: var(--label-brown);
    display: flex;
    flex-direction: column;
  }
  .label--lemon { --accent: var(--lemon); --soft: var(--band-ink-soft); }
  .label--lavender { --accent: var(--lavender); --soft: var(--band-ink-soft-lav); }

  .band {
    background: var(--accent);
    color: var(--band-ink);
    font-family: "Josefin Slab", serif;
    font-weight: 600;
    text-align: center;
    white-space: nowrap;
    overflow: hidden;
    letter-spacing: 0.02em;
  }
  .band .soft { color: var(--soft); font-weight: 400; }

  /* small 5ml label */
  .label--small { width: 332px; height: 126px; }
  .label--small .band { height: 19px; line-height: 21px; font-size: 11.5px; }
  .label--small .brand-row {
    flex: 1;
    display: flex;
    align-items: center;
    justify-content: center;
    gap: 12px;
  }
  .brand-dot { width: 32px; height: 32px; border-radius: 50%; background: var(--accent); flex: none; }
  .brand-name {
    color: var(--accent);
    font-family: "Questrial", sans-serif;
    font-size: 30px;
    letter-spacing: 0.01em;
    white-space: nowrap;
  }

  /* large 15ml label */
  .label--large { width: 388px; height: 168px; }
  .label--large .band--top {
    height: 23px; line-height: 24px; font-size: 15px;
    font-family: "Questrial", sans-serif; font-weight: 400;
  }
  .label--large .band--bottom { height: 19px; line-height: 21px; font-size: 11px; font-weight: 400; }
  .oil {
    flex: 1;
    display: flex;
    flex-direction: column;
    align-items: center;
    justify-content: center;
    color: var(--accent);
    font-family: "Nunito Sans", sans-serif;
    line-height: 1.05;
  }
  .oil .brand-dot { width: 40px; height: 40px; margin-bottom: 8px; }
  .oil-lead { font-weight: 300; font-size: 19px; }
  .oil-name { font-weight: 700; font-size: 20px; }

  .pos-lemon-small { left: 165px; top: 191px; }
  .pos-lavender-small { left: 761px; top: 191px; }
  .pos-lemon-large { left: 189px; top: 584px; }
  .pos-lavender-large { left: 785px; top: 584px; }
</style>
</head>
<body>

  <section class="label label--small label--lemon pos-lemon-small">
    <div class="band">BRIGHT LEMON • <span class="soft">PURE ESSENTIAL OIL</span> • BRIGHT LEMON</div>
    <div class="brand-row">
      <span class="brand-dot"></span>
      <span class="brand-name">verdant hollow</span>
    </div>
    <div class="band">BRIGHT LEMON • <span class="soft">PURE ESSENTIAL OIL</span> • BRIGHT LEMON</div>
  </section>

  <section class="label label--small label--lavender pos-lavender-small">
    <div class="band">ALL ABOUT LAVENDER • <span class="soft">PURE ESSENTIAL OIL</span></div>
    <div class="brand-row">
      <span class="brand-dot"></span>
      <span class="brand-name">verdant hollow</span>
    </div>
    <div class="band">ALL ABOUT LAVENDER • <span class="soft">PURE ESSENTIAL OIL</span></div>
  </section>

  <section class="label label--large label--lemon pos-lemon-large">
    <div class="band band--top">verdant hollow</div>
    <div class="oil">
      <span class="brand-dot"></span>
      <span class="oil-lead">bright</span>
      <span class="oil-name">lemon</span>
    </div>
    <div class="band band--bottom"><span class="soft">PURE ESSENTIAL OIL</span></div>
  </section>

  <section class="label label--large label--lavender pos-lavender-large">
    <div class="band band--top">verdant hollow</div>
    <div class="oil">
      <span class="brand-dot"></span>
      <span class="oil-lead">all about</span>
      <span class="oil-name">lavender</span>
    </div>
    <div class="band band--bottom"><span class="soft">PURE ESSENTIAL OIL</span></div>
  </section>

</body>
</html>
```